Business Card Design Project

We require a business card template to cover basic contact information - our company logo, names of employees, title, mobile and email.

Target Market(s)

Corporate

Industry/Entity Type

Business

Font styles to use
Sans Serif

Requirements
Nice to have
• Thinking it would be great just to have the logo taking up approximately half the space (so it goes as far across the top of the card as possible) and then contact details in the lower half of the card. Keen just to use only the two colours in the logo, on a white background.
Should not have
• No fussy drawings

```html
<!DOCTYPE html>
<html lang="en">
<head>
<meta charset="utf-8">
<title>Larkmere Developments – Business Card</title>
<link rel="stylesheet" href="https://fonts.googleapis.com/css2?family=Arimo:wght@400&display=swap">
<style>
  :root {
    --teal: #2ba3b4;
    --blue: #2f62a8;
    --card: #ffffff;
    --divider: #d6d6d6;
    --backdrop: #1c1c1c;
  }
  * { margin: 0; padding: 0; box-sizing: border-box; }
  html, body {
    width: 1200px;
    height: 800px;
    overflow: hidden;
    background: var(--backdrop);
  }
  .stage {
    width: 1200px;
    height: 800px;
    display: flex;
    align-items: center;
    justify-content: center;
  }
  .business-card {
    position: relative;
    width: 900px;
    height: 514px;
    background: var(--card);
    font-family: "Arimo", Arial, sans-serif;
    font-weight: 400;
  }
  .corner-bracket {
    position: absolute;
    width: 110px;
    height: 110px;
  }
  .corner-bracket--top-left {
    top: 0; left: 0;
    border-top: 9px solid var(--teal);
    border-left: 9px solid var(--teal);
  }
  .corner-bracket--bottom-right {
    bottom: 0; right: 0;
    border-bottom: 9px solid var(--blue);
    border-right: 9px solid var(--blue);
  }
  .brand {
    position: absolute;
    top: 34px;
    left: 60px;
    color: var(--teal);
    line-height: 1;
  }
  .brand-name {
    display: block;
    font-size: 84px;
    letter-spacing: -1px;
  }
  .brand-tagline {
    display: block;
    text-align: right;
    font-size: 20px;
    margin-top: 2px;
  }
  .person-name {
    position: absolute;
    top: 215px;
    left: 120px;
    font-size: 34px;
    color: var(--blue);
    letter-spacing: 1px;
  }
  .section-divider {
    position: absolute;
    left: 450px;
    top: 170px;
    width: 2px;
    height: 150px;
    background: var(--divider);
  }
  .contact-details {
    position: absolute;
    top: 250px;
    left: 500px;
    list-style: none;
    color: var(--teal);
    font-size: 22px;
    line-height: 1.3;
    letter-spacing: 1px;
  }
  .website {
    position: absolute;
    top: 405px;
    left: 140px;
    font-size: 36px;
    color: var(--blue);
    letter-spacing: 1px;
  }
</style>
</head>
<body>
  <main class="stage">
    <article class="business-card">
      <span class="corner-bracket corner-bracket--top-left"></span>
      <span class="corner-bracket corner-bracket--bottom-right"></span>

      <div class="brand">
        <span class="brand-name">Larkmere</span>
        <span class="brand-tagline">developments</span>
      </div>

      <p class="person-name">YOUR NAME</p>

      <span class="section-divider"></span>

      <ul class="contact-details">
        <li>XXXXX XXXXX XXXXX</li>
        <li>PH : 555 - 555 - 555</li>
        <li>EMAIL : yourmail@your.com</li>
      </ul>

      <p class="website">WWW.YOURSITE.COM</p>
    </article>
  </main>
</body>
</html>
```